New webpage design for development bureau

We are a development bureau in Denmark, and need a design for our webpage. We are called Tindral Development (Part of Tindral Brisk Skolary Group), and are going to aim for multiple markets: Web, Apps, Desktop applications, ect.

We already have a logo, see the uploaded file. We do not have any special demands, other than in have to be simple. A portfolio view should also be available, for future customers.

```html
<!DOCTYPE html>
<html lang="en">
<head>
<meta charset="utf-8">
<title>Tindral Development</title>
<link href="https://fonts.googleapis.com/css2?family=Oswald:wght@400;500;700&family=Open+Sans:wght@400;600;700&family=Kaushan+Script&display=swap" rel="stylesheet">
<style>
:root{
  --cyan:#17c5ec;
  --ink:#2b2b2b;
  --muted:#6d6d6d;
  --white:#ffffff;
  --night:#1d0f33;
  --hero-a:#2a0f55;
  --hero-b:#5b1e86;
  --band-a:#3b2e5a;
  --band-b:#8d6a6e;
  --band-c:#b88c6a;
  --light:#f3f3f3;
  --line:#e2e2e2;
}
*{box-sizing:border-box;margin:0;padding:0}
html,body{width:1200px;height:4198px;overflow:hidden}
body{font-family:"Open Sans",Arial,sans-serif;color:var(--ink);background:var(--white);font-size:13px;line-height:1.6}
h1,h2,h3,h4,.nav,.btn{font-family:"Oswald",Arial,sans-serif}
.section-title{font-family:"Oswald",Arial,sans-serif;font-weight:400;font-size:27px;text-transform:uppercase;text-align:center;letter-spacing:.5px}
.dots{display:flex;justify-content:center;gap:6px;margin:14px 0 0}
.dots i{width:6px;height:6px;border-radius:50%;background:var(--cyan)}
.title-rule{width:330px;margin:0 auto;border-top:1px solid rgba(255,255,255,.45);padding-top:0}

/* hero */
.hero{position:relative;height:800px;background:radial-gradient(ellipse at 30% 40%,#4f1b7c 0%,var(--hero-a) 70%);color:var(--white)}
.topbar{position:absolute;top:0;left:0;right:0;height:80px;display:flex;align-items:center;justify-content:space-between;padding:0 52px}
.brand{font-family:"Oswald",sans-serif;font-weight:700;font-size:30px;letter-spacing:1px}
.nav{display:flex;gap:22px;font-size:15px;text-transform:uppercase}
.nav a{color:var(--white);text-decoration:none}
.nav a.active{color:var(--cyan)}
.hero-photo{position:absolute;left:630px;top:90px;width:570px;height:710px;background:linear-gradient(150deg,#6a3a96 0%,#3a1c5c 55%,#c9a48b 100%);border-radius:40px 0 0 0}
.hero-copy{position:absolute;left:52px;top:225px;width:460px}
.hero-copy h1{font-size:62px;line-height:1.08;font-weight:700;text-transform:uppercase}
.hero-copy p{margin-top:24px;font-size:15px;line-height:1.5}
.btn{display:inline-block;background:var(--cyan);color:var(--white);text-transform:uppercase;font-size:16px;padding:14px 26px;margin-top:34px}

/* welcome */
.welcome{height:320px;padding-top:70px;text-align:center}
.welcome p{width:1120px;margin:36px auto 0;font-size:12.5px;color:var(--muted);line-height:1.75}

/* features */
.features{height:497px;background:linear-gradient(160deg,var(--band-a) 0%,#6b5370 55%,var(--band-c) 100%);color:var(--white);padding-top:70px}
.features .title-rule{padding-top:0;border:none}
.feature-grid{display:grid;grid-template-columns:repeat(3,1fr);gap:46px 60px;width:1100px;margin:60px auto 0}
.feature{display:flex;gap:22px}
.feature .ico{flex:none;width:52px;height:52px;border:2px solid var(--white);border-radius:50%;display:flex;align-items:center;justify-content:center}
.feature h4{font-size:17px;font-weight:400}
.feature p{font-size:12px;line-height:1.55;margin-top:6px;opacity:.9}

/* works */
.works{height:553px;padding-top:65px}
.works .title-rule{border-color:var(--line)}
.work-row{display:flex;gap:32px;justify-content:center;margin-top:58px}
.work{width:253px;height:253px}
.pager{display:flex;gap:6px;justify-content:center;margin-top:30px}
.pager span{width:28px;height:28px;background:#c9c9c9;display:flex;align-items:center;justify-content:center}

/* team */
.team{height:508px;background:linear-gradient(170deg,#423a5c 0%,#6e5b6e 50%,#a98374 100%);color:var(--white);padding-top:62px}
.members{display:flex;justify-content:center;gap:72px;margin-top:52px}
.member{text-align:center;width:210px}
.avatar{width:210px;height:210px;border-radius:50%;border:6px solid rgba(255,255,255,.85);background:linear-gradient(160deg,#c8b8ac,#6c5f5a)}
.member h4{font-size:17px;font-weight:400;margin-top:22px}
.member span{font-size:13px;opacity:.85}

/* blog & testimonial */
.split{height:700px;display:flex;gap:50px;padding:72px 52px 0}
.blog{width:550px}
.blog h3,.says h3{font-size:27px;font-weight:400;text-transform:uppercase;text-align:center}
.posts{display:flex;gap:40px;margin-top:48px}
.post{width:255px;text-align:center}
.post .thumb{height:160px;background:linear-gradient(140deg,#d8dde2,#6f8aa5)}
.post h4{font-size:15px;font-weight:500;margin-top:20px}
.post .meta{font-size:11px;color:#999;margin-top:2px}
.post p{font-size:12px;color:var(--muted);margin-top:6px}
.post .more{display:inline-block;background:var(--light);border:1px solid var(--line);font-size:11px;padding:5px 14px;margin-top:12px}
.says{flex:1}
.quote-box{position:relative;background:var(--light);margin-top:48px;height:310px;padding:48px 42px;font-size:12.5px;color:var(--muted);text-align:center}
.quote-box .who{margin-top:20px;color:var(--ink);font-weight:600}
.quote-face{position:absolute;left:50%;bottom:-40px;margin-left:-40px;width:80px;height:80px;border-radius:50%;border:4px solid var(--white);background:linear-gradient(160deg,#d9b9a0,#8a6b58)}
.quote-nav{display:flex;gap:6px;justify-content:flex-end;margin-top:-28px;margin-right:8px;position:relative}
.quote-nav span{width:24px;height:24px;background:#d0d0d0}

/* clients */
.clients{height:339px;background:linear-gradient(165deg,#2d2745 0%,#6a5660 55%,#b68967 100%);color:var(--white);padding-top:50px}
.logo-row{display:flex;justify-content:center;gap:56px;margin-top:52px}
.client{width:187px;height:110px;background:var(--white);display:flex;align-items:center;justify-content:center;gap:10px;color:#333;font-family:"Open Sans",sans-serif;font-weight:700;font-size:22px}
.client i{width:18px;height:18px;border-radius:50%;background:#333}

/* newsletter */
.newsletter{height:98px;background:var(--cyan);display:flex;align-items:center;padding:0 52px;gap:22px}
.newsletter h3{font-family:"Kaushan Script",cursive;font-weight:400;font-size:34px;color:var(--white);width:330px}
.field{width:270px;height:40px;background:var(--white);font-size:13px;color:#777;padding:10px 12px}
.newsletter .go{background:var(--night);color:var(--white);font-family:"Oswald",sans-serif;text-transform:uppercase;font-size:14px;padding:10px 26px}

/* footer */
.footer{position:relative;height:332px;background:var(--night);color:#cfc8de;padding-top:38px;text-align:center}
.footer h4{font-size:17px;font-weight:400;color:var(--white);text-transform:uppercase}
.footer .title-rule{width:360px;margin-top:16px;border-color:rgba(255,255,255,.2)}
.cols{display:flex;justify-content:space-around;padding:0 70px;margin-top:32px}
.col{width:230px}
.col .ico{width:52px;height:52px;border:1.5px solid #bfb7d2;border-radius:50%;margin:0 auto;display:flex;align-items:center;justify-content:center}
.col h5{font-family:"Oswald",sans-serif;font-weight:400;font-size:15px;color:var(--white);margin-top:14px;text-transform:uppercase}
.col p{font-size:12px;line-height:1.6;margin-top:4px}
.to-top{position:absolute;left:50%;bottom:-24px;margin-left:-24px;width:48px;height:48px;border-radius:50%;background:var(--cyan);display:flex;align-items:center;justify-content:center;z-index:2}
.bottom{height:51px;background:#130a24;display:flex;align-items:center;justify-content:space-between;padding:0 52px;color:#aaa;font-size:12px}
.social{display:flex;gap:6px}
.social i{width:22px;height:22px;border-radius:50%;background:var(--cyan)}
</style>
</head>
<body>

<header class="hero">
  <div class="topbar">
    <div class="brand">TINDRAL</div>
    <nav class="nav">
      <a class="active" href="#">Home</a><a href="#">About us</a><a href="#">Features</a><a href="#">Our team</a><a href="#">Testimonials</a><a href="#">Blog</a><a href="#">Our clients</a><a href="#">Contact</a>
    </nav>
  </div>
  <div class="hero-photo" role="img" aria-label="Hand holding a smartphone showing the app, with colourful floating shapes"></div>
  <div class="hero-copy">
    <h1>Showcase your apps with easy!</h1>
    <p>Nullam ac urna eu felis dapibus condimentum sit amet a augue. Sed non neque elit. Sed ut imperdiet nisi. Proin condimentum fermentum nunc. Etiam pharetra, erat sed fermentum feugiat, velit mauris egestas quam.</p>
    <span class="btn">Download the app</span>
  </div>
</header>

<section class="welcome">
  <h2 class="section-title">Welcome to Tindral Group</h2>
  <div class="dots"><i></i><i></i><i></i></div>
  <p>This is a short overview of who we are. We build web sites, mobile apps and desktop software for clients across many markets. Our small team plans, designs and develops each project with care, keeping every solution simple, fast and easy to maintain. From first sketch to final launch we work closely with you, and we stay around afterwards to support, improve and grow the product together with your business.</p>
</section>

<section class="features">
  <h2 class="section-title">Tindral Features</h2>
  <div class="dots"><i></i><i></i><i></i></div>
  <div class="feature-grid">
    <div class="feature"><span class="ico"><svg width="22" height="22" viewBox="0 0 22 22" fill="none" stroke="#fff" stroke-width="2"><circle cx="11" cy="11" r="8"/><path d="M9 7l6 4-6 4z" fill="#fff"/></svg></span><div><h4>Audio &amp; Video Previews</h4><p>Nam nec tellus a odio tincidunt auctor a ornare odio. Sed non mauris vitae erat consequat auctor eu in elit.</p></div></div>
    <div class="feature"><span class="ico"><svg width="22" height="22" viewBox="0 0 22 22" fill="none" stroke="#fff" stroke-width="2"><rect x="3" y="4" width="16" height="11" rx="2"/><path d="M7 15l-2 4 5-4"/></svg></span><div><h4>Notification Viewing</h4><p>Nam nec tellus a odio tincidunt auctor a ornare odio. Sed non mauris vitae erat consequat auctor eu in elit.</p></div></div>
    <div class="feature"><span class="ico"><svg width="22" height="22" viewBox="0 0 22 22" fill="none" stroke="#fff" stroke-width="2"><rect x="3" y="5" width="16" height="12" rx="1"/><path d="M3 15l5-5 4 4 3-3 4 4"/></svg></span><div><h4>Share Pictures</h4><p>Nam nec tellus a odio tincidunt auctor a ornare odio. Sed non mauris vitae erat consequat auctor eu in elit.</p></div></div>
    <div class="feature"><span class="ico"><svg width="22" height="22" viewBox="0 0 22 22" fill="none" stroke="#fff" stroke-width="2"><path d="M3 5h11v8H8l-3 3v-3H3z"/><path d="M16 9h3v7h-2v2l-3-2h-3"/></svg></span><div><h4>Discussion &amp; Notes Details</h4><p>Nam nec tellus a odio tincidunt auctor a ornare odio. Sed non mauris vitae erat consequat auctor eu in elit.</p></div></div>
    <div class="feature"><span class="ico"><svg width="22" height="22" viewBox="0 0 22 22" fill="none" stroke="#fff" stroke-width="2"><path d="M4 6h14M4 11h14M4 16h14"/></svg></span><div><h4>Lists &amp; Files Browse</h4><p>Nam nec tellus a odio tincidunt auctor a ornare odio. Sed non mauris vitae erat consequat auctor eu in elit.</p></div></div>
    <div class="feature"><span class="ico"><svg width="22" height="22" viewBox="0 0 22 22" fill="none" stroke="#fff" stroke-width="2"><path d="M6 15a4 4 0 010-8 5 5 0 019-1 4 4 0 011 9z"/><path d="M11 9v6M8.5 12.5L11 15l2.5-2.5"/></svg></span><div><h4>Attach Files</h4><p>Nam nec tellus a odio tincidunt auctor a ornare odio. Sed non mauris vitae erat consequat auctor eu in elit.</p></div></div>
  </div>
</section>

<section class="works">
  <h2 class="section-title">Our Works</h2>
  <div class="dots"><i></i><i></i><i></i></div>
  <div class="work-row">
    <div class="work" role="img" aria-label="Dark dashboard app interface with charts" style="background:linear-gradient(150deg,#3f4a4c,#7aa7a0)"></div>
    <div class="work" role="img" aria-label="Colourful calendar app interface" style="background:linear-gradient(150deg,#f1e6cc,#e7b66a)"></div>
    <div class="work" role="img" aria-label="Wireframe sketches on paper with a pen" style="background:linear-gradient(150deg,#7a3e86,#d9d2d8)"></div>
    <div class="work" role="img" aria-label="Tablet showing a web application" style="background:linear-gradient(150deg,#c9ccd0,#7d8591)"></div>
  </div>
  <div class="pager">
    <span><svg width="10" height="10" viewBox="0 0 10 10"><path d="M7 1L3 5l4 4" stroke="#fff" stroke-width="2" fill="none"/></svg></span>
    <span><svg width="10" height="10" viewBox="0 0 10 10"><path d="M3 1l4 4-4 4" stroke="#fff" stroke-width="2" fill="none"/></svg></span>
  </div>
</section>

<section class="team">
  <h2 class="section-title">Meet Our Team</h2>
  <div class="dots"><i></i><i></i><i></i></div>
  <div class="members">
    <div class="member"><div class="avatar" role="img" aria-label="Portrait of team member"></div><h4>Anton Vestby</h4><span>Project Manager</span></div>
    <div class="member"><div class="avatar" role="img" aria-label="Portrait of team member"></div><h4>Lars Kromann</h4><span>Web Designer</span></div>
    <div class="member"><div class="avatar" role="img" aria-label="Portrait of team member"></div><h4>Mikkel Tarp</h4><span>Graphic Designer</span></div>
    <div class="member"><div class="avatar" role="img" aria-label="Portrait of team member"></div><h4>Soren Lund</h4><span>Usability Expert</span></div>
  </div>
</section>

<section class="split">
  <div class="blog">
    <h3>Recent Blog Posts</h3>
    <div class="dots"><i></i><i></i><i></i></div>
    <div class="posts">
      <article class="post"><div class="thumb" role="img" aria-label="Team working together at a laptop"></div><h4>Image with text blog post</h4><div class="meta">20 March 2014 | 0 Comments</div><p>Nam nec tellus a odio tincidunt auctor a ornare odio. Sed non mauris vitae erat consequat auctor eu in elit.</p><span class="more">Read More</span></article>
      <article class="post"><div class="thumb" role="img" aria-label="Businessman in a suit smiling" style="background:linear-gradient(140deg,#e4e8ec,#4f6d8a)"></div><h4>Video with text blog post</h4><div class="meta">20 March 2014 | 0 Comments</div><p>Nam nec tellus a odio tincidunt auctor a ornare odio. Sed non mauris vitae erat consequat auctor eu in elit.</p><span class="more">Read More</span></article>
    </div>
  </div>
  <div class="says">
    <h3>What About Clients Says</h3>
    <div class="dots"><i></i><i></i><i></i></div>
    <div class="quote-box">
      <p>Nam nec tellus a odio tincidunt auctor a ornare odio. Sed non mauris vitae erat consequat auctor eu in elit. Class aptent taciti sociosqu ad litora torquent per conubia nostra, per inceptos himenaeos. Proin gravida nibh vel velit auctor aliquet. Aenean sollicitudin, lorem quis bibendum auctor, nisi elit consequat ipsum, nec sagittis sem nibh id elit. Duis sed odio sit amet nibh vulputate cursus a sit amet mauris.</p>
      <div class="who">- Henrik Dalsgaard</div>
      <div class="quote-face" role="img" aria-label="Client portrait"></div>
    </div>
    <div class="quote-nav"><span></span><span></span></div>
  </div>
</section>

<section class="clients">
  <h2 class="section-title">Our Clients</h2>
  <div class="dots"><i></i><i></i><i></i></div>
  <div class="logo-row">
    <div class="client"><i></i>NORVIK</div>
    <div class="client"><i></i>NORVIK</div>
    <div class="client"><i></i>NORVIK</div>
    <div class="client"><i></i>NORVIK</div>
    <div class="client"><i></i>NORVIK</div>
  </div>
</section>

<section class="newsletter">
  <h3>Our Newsletter Signup</h3>
  <div class="field">Enter Your Name</div>
  <div class="field">Enter Your Email</div>
  <span class="go">Subscribe Now</span>
</section>

<footer class="footer">
  <h4>Get In Touch</h4>
  <div class="title-rule"></div>
  <div class="cols">
    <div class="col"><span class="ico"><svg width="20" height="20" viewBox="0 0 20 20" fill="none" stroke="#fff" stroke-width="1.6"><path d="M10 18s-6-6-6-10a6 6 0 0112 0c0 4-6 10-6 10z"/><circle cx="10" cy="8" r="2"/></svg></span><h5>Tindral Group</h5><p>Nam nec tellus a odio tincidunt auctor a<br>ornare odio sit elit - 56887</p></div>
    <div class="col"><span class="ico"><svg width="20" height="20" viewBox="0 0 20 20" fill="none" stroke="#fff" stroke-width="1.6"><path d="M5 2h3l1.5 4-2 1.5a10 10 0 005 5l1.5-2 4 1.5v3a2 2 0 01-2 2A15 15 0 013 4a2 2 0 012-2z"/></svg></span><h5>Call Us</h5><p>(555)010 24 1187<br>(555)010 24 3390</p></div>
    <div class="col"><span class="ico"><svg width="20" height="20" viewBox="0 0 20 20" fill="none" stroke="#fff" stroke-width="1.6"><rect x="2" y="4" width="16" height="12"/><path d="M2 4l8 7 8-7"/></svg></span><h5>Email Us</h5><p>All query to message Now<br>info@tindralgroup.com</p></div>
    <div class="col"><span class="ico"><svg width="20" height="20" viewBox="0 0 20 20" fill="none" stroke="#fff" stroke-width="1.6"><circle cx="10" cy="10" r="8"/><path d="M2 10h16M10 2c3 3 3 13 0 16M10 2c-3 3-3 13 0 16"/></svg></span><h5>Website</h5><p>All information &amp; Services available<br>www.tindralgroup.com</p></div>
  </div>
  <span class="to-top"><svg width="16" height="16" viewBox="0 0 16 16"><path d="M3 10l5-5 5 5" stroke="#fff" stroke-width="2.2" fill="none"/></svg></span>
</footer>
<div class="bottom">
  <span>©2014 Tindral Group All Rights Reserved</span>
  <div class="social"><i></i><i></i><i></i></div>
</div>

</body>
</html>
```